Solar energy proposal for homeowners

I am providing households with solar energy proposals, and I need a high-quality brochure that is packaged cleverly to attract the homeowner's attention. Take a look at the one page solar brochure that I have included to get an idea of text and content.

Target Market(s)

Residential Homeowners

Industry/Entity Type

Solar

Requirements
Must have
• High quality document

```html
<!DOCTYPE html>
<html lang="en">
<head>
<meta charset="utf-8">
<title>Helvora Energy – Solar for $0 Down</title>
<link rel="stylesheet" href="https://fonts.googleapis.com/css2?family=Outfit:wght@300;400;500;600;700;800&display=swap">
<style>
  :root {
    --navy: #3b4672;
    --navy-soft: #6b759c;
    --teal: #1fd3c6;
    --band-blue: #0a8ddb;
    --band-teal: #00c2c9;
    --green: #4fd67a;
    --photo-warm: #c99aa6;
    --photo-cool: #6c7892;
    --white: #ffffff;
    --footer: #2c2c2e;
  }
  * { box-sizing: border-box; margin: 0; padding: 0; }
  html, body { width: 849px; height: 1200px; overflow: hidden; }
  body { font-family: "Outfit", sans-serif; color: var(--white); background: var(--navy); }

  .brochure { position: relative; width: 849px; height: 1200px; background: var(--navy); overflow: hidden; }

  .brand { position: absolute; left: 46px; top: 84px; display: flex; align-items: center; gap: 14px; }
  .brand-mark { width: 22px; height: 22px; background: var(--teal); }
  .brand-name { font-size: 44px; font-weight: 400; color: var(--teal); letter-spacing: 1px; line-height: 1; }

  .hero-band {
    position: absolute; left: 0; top: 187px; width: 461px; height: 319px;
    background: linear-gradient(90deg, var(--band-blue), var(--band-teal));
  }
  .accent-band { position: absolute; left: 789px; top: 187px; width: 60px; height: 319px; background: var(--green); }
  .hero-photo {
    position: absolute; left: 461px; top: 0; width: 328px; height: 577px;
    background: linear-gradient(180deg, var(--photo-warm), var(--photo-cool));
  }

  .headline {
    position: absolute; left: 45px; top: 197px;
    font-size: 54px; font-weight: 700; line-height: 59px; letter-spacing: -0.5px; text-transform: uppercase;
  }
  .tagline { position: absolute; left: 46px; top: 443px; font-size: 22.5px; font-weight: 400; line-height: 24.6px; }

  .section-title { font-size: 26px; font-weight: 700; line-height: 1; }

  .about { position: absolute; left: 51px; top: 560px; width: 322px; }
  .about p { margin-top: 11px; font-size: 17.3px; line-height: 24.2px; font-weight: 400; }

  .why { position: absolute; left: 462px; top: 616px; }
  .why ul { list-style: none; margin-top: 14px; }
  .why li { display: flex; align-items: center; font-size: 17px; line-height: 24.2px; }
  .why li::before {
    content: ""; width: 0; height: 0; margin-right: 16px;
    border-top: 6px solid transparent; border-bottom: 6px solid transparent; border-left: 11px solid var(--teal);
  }
  .why .no { color: var(--teal); margin-right: 4px; }

  .hex-decor {
    position: absolute; left: 720px; top: 697px; width: 129px; height: 323px;
    background: linear-gradient(180deg, rgba(107,117,156,0.55), rgba(107,117,156,0.35));
  }

  .services-title { position: absolute; left: 51px; top: 790px; }

  .service { position: absolute; display: flex; gap: 16px; }
  .service svg { flex: none; width: 42px; height: 48px; }
  .service h3 { font-size: 26.5px; font-weight: 500; color: var(--teal); line-height: 1; margin-top: 1px; letter-spacing: -0.2px; white-space: nowrap; }
  .service p { font-size: 17px; line-height: 24.2px; margin-top: 6px; }
  .service-affordable { left: 51px; top: 834px; width: 380px; }
  .service-affordable p { width: 235px; }
  .service-install { left: 440px; top: 834px; width: 300px; }
  .service-install p { width: 235px; }
  .service-local { left: 51px; top: 990px; width: 330px; }
  .service-local p { width: 262px; }
  .service-eco { left: 440px; top: 990px; width: 300px; }
  .service-eco p { width: 235px; }

  .footer {
    position: absolute; left: 0; top: 1137px; width: 849px; height: 63px; background: var(--footer);
    display: flex; align-items: center; justify-content: center; gap: 48px; font-size: 17.5px; font-weight: 500;
  }
  .contact { display: flex; align-items: center; gap: 9px; }
  .contact svg { width: 16px; height: 16px; }
</style>
</head>
<body>
<main class="brochure">
  <div class="brand">
    <span class="brand-mark"></span>
    <span class="brand-name">helvora energy</span>
  </div>

  <div class="hero-band"></div>
  <div class="accent-band"></div>
  <div class="hero-photo" role="img" aria-label="Photo of a modern home with rooftop solar panels and a pool at sunset"></div>

  <h1 class="headline">Solar for $0<br>down.<br>No liens.<br>No kidding.</h1>
  <p class="tagline">Power Your Future with<br>Helvora Energy</p>

  <section class="about">
    <h2 class="section-title">About Us</h2>
    <p>At Helvora Energy, our mission is to make solar simple and accessible for everyone. No high-pressure sales-just the information you need to make a smart choice. With our solar rental program, you can lower your monthly energy costs and pay less than your current electricity bill.</p>
  </section>

  <section class="why">
    <h2 class="section-title">Why Choose Us?</h2>
    <ul>
      <li><span class="no">No</span>financing</li>
      <li><span class="no">No</span>liens</li>
      <li><span class="no">No</span>down payment</li>
      <li><span class="no">No</span>insurance costs</li>
      <li><span class="no">No</span>long-term commitment</li>
      <li><span class="no">No</span>maintenance costs</li>
    </ul>
  </section>

  <div class="hex-decor" role="img" aria-label="Faint honeycomb pattern decoration"></div>

  <h2 class="section-title services-title">Our Best Services</h2>

  <svg width="0" height="0" style="position:absolute">
    <defs>
      <linearGradient id="hexFill" x1="0" y1="0" x2="0" y2="1">
        <stop offset="0" stop-color="#1fd3c6"/>
        <stop offset="1" stop-color="#0a8ddb"/>
      </linearGradient>
    </defs>
  </svg>

  <article class="service service-affordable">
    <svg viewBox="0 0 42 48"><polygon points="21,0 42,12 42,36 21,48 0,36 0,12" fill="url(#hexFill)"/><circle cx="21" cy="22" r="6" fill="none" stroke="#3b4672" stroke-width="2"/><path d="M11 32 h20" stroke="#3b4672" stroke-width="2.5" stroke-linecap="round"/></svg>
    <div><h3>Affordable &amp; Transparent</h3><p>Simple pricing, no hidden fees and a fixed monthly rate lower than typical energy bills</p></div>
  </article>

  <article class="service service-install">
    <svg viewBox="0 0 42 48"><polygon points="21,0 42,12 42,36 21,48 0,36 0,12" fill="url(#hexFill)"/><circle cx="21" cy="17" r="4" fill="#3b4672"/><rect x="14" y="23" width="14" height="9" rx="2" fill="#3b4672"/></svg>
    <div><h3>Expert Installation</h3><p>Certified professionals handle installation, maintenance, and repairs end to end.</p></div>
  </article>

  <article class="service service-local">
    <svg viewBox="0 0 42 48"><polygon points="21,0 42,12 42,36 21,48 0,36 0,12" fill="url(#hexFill)"/><path d="M21 12a6 6 0 0 1 6 6c0 5-6 10-6 10s-6-5-6-10a6 6 0 0 1 6-6z" fill="#3b4672"/><rect x="14" y="31" width="14" height="4" rx="1" fill="#3b4672"/></svg>
    <div><h3>Local Expertise</h3><p>Florida-based team that understands the needs of Orlando and statewide homeowners</p></div>
  </article>

  <article class="service service-eco">
    <svg viewBox="0 0 42 48"><polygon points="21,0 42,12 42,36 21,48 0,36 0,12" fill="url(#hexFill)"/><path d="M13 30c0-9 7-14 16-14 0 9-5 16-16 14z" fill="#3b4672"/></svg>
    <div><h3>Eco-Friendly</h3><p>Clean, renewable solar energy that helps reduce your carbon footprint.</p></div>
  </article>

  <footer class="footer">
    <span class="contact">
      <svg viewBox="0 0 16 16"><circle cx="8" cy="8" r="8" fill="#fff"/><rect x="5.5" y="3.5" width="5" height="9" rx="1" fill="#2c2c2e"/></svg>
      (407) 555-0142
    </span>
    <span class="contact">
      <svg viewBox="0 0 16 16"><circle cx="8" cy="8" r="8" fill="#fff"/><path d="M8 3.5a3 3 0 0 1 3 3c0 2.5-3 6-3 6s-3-3.5-3-6a3 3 0 0 1 3-3z" fill="#2c2c2e"/><circle cx="8" cy="6.5" r="1.1" fill="#fff"/></svg>
      123 Anywhere St, Any City
    </span>
    <span class="contact">
      <svg viewBox="0 0 16 16"><circle cx="8" cy="8" r="8" fill="#fff"/><circle cx="8" cy="8" r="5" fill="none" stroke="#2c2c2e" stroke-width="1.2"/><ellipse cx="8" cy="8" rx="2.2" ry="5" fill="none" stroke="#2c2c2e" stroke-width="1.2"/><path d="M3 8h10" stroke="#2c2c2e" stroke-width="1.2"/></svg>
      www.helvoraenergy.com
    </span>
  </footer>
</main>
</body>
</html>
```